QLB Insurance Services Business Card
Slogan - Quiet Lanterns Burn
Creative Brief
Use specific fonts
Feel free to use the same font as used in my logo OR whatever looks good
Simple
Marisol (Greta) Dovik
Broker
20387 Marlowpine Dr. Tustin, CA 92740
greta@qlbinsurance.example
www.qblinsurance.example
0K47382
*Commercial Liability *Commercial Property *Business Owner Policy *Excess/Umbrella Liability *Worker's Compensation *Professional Liability *Commercial/Business Auto *Homeowner/Auto Insurance *Flood/Earthquake Insurance and more *Specializing import/export and manufacture company

```html
<!DOCTYPE html>
<html lang="en">
<head>
<meta charset="utf-8">
<title>QLB Insurance Services Business Card</title>
<link href="https://fonts.googleapis.com/css2?family=Tinos:ital,wght@0,400;0,700;1,400;1,700&display=swap" rel="stylesheet">
<style>
  :root {
    --backdrop: #2b2c2e;
    --card: #fbfbfb;
    --ink: #222326;
    --muted: #3c3d40;
    --blue: #1c86d1;
    --blue-deep: #0f5f9e;
    --blue-light: #4fb0ee;
    --rule: #9a9a9a;
  }
  * { box-sizing: border-box; margin: 0; padding: 0; }
  html, body { width: 1200px; height: 852px; overflow: hidden; }
  body {
    background: var(--backdrop);
    font-family: "Tinos", "Times New Roman", serif;
    color: var(--ink);
    position: relative;
  }
  .card {
    position: absolute;
    width: 500px;
    height: 286px;
    background: var(--card);
    border-radius: 18px;
    overflow: hidden;
    box-shadow: 0 10px 24px rgba(0,0,0,.45);
  }
  .card--front { left: 130px; top: 130px; }
  .card--back { left: 570px; top: 436px; }
  .edge-band {
    position: absolute; left: 0; top: 0; bottom: 0; width: 20px;
    background: linear-gradient(180deg, var(--blue-light), var(--blue) 50%, var(--blue-deep));
  }
  .edge-line {
    position: absolute; left: 26px; top: 0; bottom: 0; width: 3px;
    background: #111;
  }
  .brand { position: absolute; text-align: center; }
  .brand__row { display: flex; align-items: center; justify-content: center; gap: 8px; }
  .brand__dot { width: 14px; height: 14px; border-radius: 50%; background: var(--blue); flex: none; }
  .brand__name { font-weight: 700; font-size: 21px; letter-spacing: .5px; color: var(--ink); white-space: nowrap; }
  .brand__slogan {
    margin-top: 3px; font-size: 13px; font-weight: 700; color: var(--blue);
    border-top: 1px solid var(--blue); display: inline-block; padding-top: 2px; letter-spacing: .5px;
  }
  .person { position: absolute; }
  .person__name { color: var(--blue); font-weight: 700; font-size: 16px; white-space: nowrap; }
  .person__role { font-style: italic; font-weight: 700; font-size: 12px; margin-top: 3px; }
  .person__license { font-size: 12px; color: var(--muted); margin-top: 5px; }
  .divider { position: absolute; width: 1px; background: var(--rule); }
  .contact { position: absolute; font-size: 12px; color: var(--muted); line-height: 1.35; }
  .contact__line { display: flex; align-items: center; gap: 7px; margin-top: 4px; white-space: nowrap; }
  .contact__line svg { width: 11px; height: 11px; flex: none; }
  .contact__address { margin-bottom: 8px; }
</style>
</head>
<body>

<article class="card card--front">
  <div class="edge-band"></div>
  <div class="edge-line"></div>

  <div class="brand" style="left:60px; right:30px; top:44px;">
    <div class="brand__row"><span class="brand__dot"></span><span class="brand__name">QLB Insurance Services</span></div>
    <span class="brand__slogan">Quiet Lanterns Burn</span>
  </div>

  <div class="person" style="left:64px; top:156px;">
    <div class="person__name">Marisol (Greta) Dovik</div>
    <div class="person__role">Broker</div>
    <div class="person__license" style="margin-top:14px;">License No : 0K47382</div>
  </div>

  <div class="divider" style="left:264px; top:148px; height:108px;"></div>

  <div class="contact" style="left:276px; top:150px;">
    <div class="contact__address">20387 Marlowpine Dr.<br>Larkhaven, NV 89740</div>
    <div class="contact__line">
      <svg viewBox="0 0 12 12"><path d="M2.5 1 L4.5 1 L5.2 3.6 L4 4.6 Q5.3 7 7.4 8 L8.4 6.8 L11 7.5 L11 9.5 Q10.5 11 9 11 Q1 10 1 3 Q1 1.5 2.5 1 Z" fill="var(--blue)"/></svg>
      <span>555-5550142</span>
    </div>
    <div class="contact__line">
      <svg viewBox="0 0 12 12"><circle cx="6" cy="3.6" r="2.6" fill="var(--blue)"/><path d="M1 11.5 Q1 6.8 6 6.8 Q11 6.8 11 11.5 Z" fill="var(--blue)"/></svg>
      <span>555-5550187</span>
    </div>
    <div class="contact__line">
      <svg viewBox="0 0 12 12"><circle cx="6" cy="6" r="5.5" fill="var(--blue)"/></svg>
      <span>greta@qlbinsurance.example</span>
    </div>
  </div>
</article>

<article class="card card--back">
  <div class="edge-band"></div>
  <div class="edge-line"></div>

  <div class="brand" style="left:44px; width:236px; top:118px;">
    <div class="brand__row"><span class="brand__dot"></span><span class="brand__name" style="font-size:17px;">QLB Insurance Services</span></div>
    <span class="brand__slogan" style="font-size:11px;">Quiet Lanterns Burn</span>
  </div>

  <div class="divider" style="left:290px; top:40px; height:210px;"></div>

  <div class="person" style="left:302px; top:38px;">
    <div class="person__name">Marisol (Greta) Dovik</div>
    <div class="person__role">Broker</div>
    <div class="person__license">License No : 0K47382</div>
  </div>

  <div class="contact" style="left:302px; top:130px;">
    <div class="contact__address">20387 Marlowpine Dr.<br>Larkhaven, NV 89740</div>
    <div class="contact__line">
      <svg viewBox="0 0 12 12"><path d="M2.5 1 L4.5 1 L5.2 3.6 L4 4.6 Q5.3 7 7.4 8 L8.4 6.8 L11 7.5 L11 9.5 Q10.5 11 9 11 Q1 10 1 3 Q1 1.5 2.5 1 Z" fill="var(--blue)"/></svg>
      <span>555-5550142</span>
    </div>
    <div class="contact__line">
      <svg viewBox="0 0 12 12"><circle cx="6" cy="3.6" r="2.6" fill="var(--blue)"/><path d="M1 11.5 Q1 6.8 6 6.8 Q11 6.8 11 11.5 Z" fill="var(--blue)"/></svg>
      <span>555-5550187</span>
    </div>
    <div class="contact__line">
      <svg viewBox="0 0 12 12"><circle cx="6" cy="6" r="5.5" fill="var(--blue)"/></svg>
      <span>greta@qlbinsurance.example</span>
    </div>
  </div>
</article>

</body>
</html>
```